Nightclub promoter business cards

We need business cards designed for our company based in Toronto, Canada called "NowMirazo". We are an events company that promotes weekly parties in the city. We cater to a 25+ crowd and feel like our brand should reflect that. We are looking for business cards that are textured and contain a unique design. We would prefer black cards. The final design should communicate the finest hospitality and prestige. I've attached files containing our logo. For more info. about our brand visit our website at www.nowmirazo.example.

Industry/Entity Type

Business

```html
<!DOCTYPE html>
<html lang="en">
<head>
<meta charset="utf-8">
<title>NowMirazo Business Card</title>
<link rel="stylesheet" href="https://fonts.googleapis.com/css2?family=Pathway+Gothic+One&family=Questrial&family=Arimo&display=swap">
<style>
  :root {
    --card-black: #000000;
    --leather-light: #6a6a6a;
    --leather-mid: #2c2c2c;
    --text-white: #ffffff;
    --text-soft: #e8e8e8;
  }
  * { margin: 0; padding: 0; box-sizing: border-box; }
  html, body {
    width: 1200px; height: 702px; overflow: hidden;
    background: var(--card-black);
  }
  .card {
    position: relative; width: 1200px; height: 702px;
    background: var(--card-black); overflow: hidden;
  }
  .leather-texture {
    position: absolute; left: 360px; top: 0; width: 840px; height: 702px;
    background:
      radial-gradient(ellipse 62% 70% at 72% 22%, var(--leather-light) 0%, var(--leather-mid) 45%, rgba(0,0,0,0) 80%),
      linear-gradient(90deg, var(--card-black) 0%, rgba(0,0,0,0) 35%, rgba(0,0,0,0) 100%);
  }
  .brand-name {
    position: absolute; left: 60px; top: 40px;
    font-family: "Pathway Gothic One", sans-serif;
    font-size: 100px; line-height: 1; color: var(--text-white);
    letter-spacing: 0.5px;
  }
  .phone {
    position: absolute; left: 62px; top: 176px;
    display: flex; align-items: center; gap: 8px;
    font-family: "Arimo", sans-serif; font-size: 25px;
    letter-spacing: 4px; color: var(--text-soft);
  }
  .phone-icon { width: 16px; height: 26px; }
  .social {
    position: absolute; left: 63px; top: 604px;
    display: flex; align-items: center; gap: 8px;
    font-family: "Arimo", sans-serif; font-size: 22px;
    color: var(--text-white);
  }
  .social-mark { width: 32px; height: 36px; background: #4a4a4a; }
  .tagline {
    position: absolute; right: 72px; top: 612px;
    font-family: "Questrial", sans-serif; font-size: 32px;
    color: var(--text-white); letter-spacing: 0.3px;
  }
</style>
</head>
<body>
  <div class="card">
    <div class="leather-texture" role="img" aria-label="Close-up of black embossed crocodile-pattern leather, lit from the upper right"></div>

    <div class="brand-name">nowmirazo</div>

    <div class="phone">
      <svg class="phone-icon" viewBox="0 0 16 26" aria-hidden="true">
        <path d="M5 1 L9 1 L9 7 L6 8 Q5 13 6 18 L9 19 L9 25 L5 25 Q1 21 1 13 Q1 5 5 1 Z" fill="var(--text-soft)"/>
      </svg>
      <span>647-555-0142</span>
    </div>

    <div class="social">
      <span class="social-mark" aria-hidden="true"></span>
      <span>https://www.socialpage.example/nowmirazo</span>
    </div>

    <div class="tagline">If it’s MIRAZO, you’ll know...</div>
  </div>
</body>
</html>
```